Finance Broker helping people meet their personal and business goals

New business card design,
1st look at the old business card so this makes sense.
I DON'T want:
the subtext "For all your Rural and Commercial Finance".
I DON'T want the: "and Management Consultant" words
I DON'T want the old phone: 07 49217305
I DON'T want the fax number: 07 48160923
I DON'T want the email address: tallowcreek@quarnet.com.au
I DON'T want the flower
What I DO want
I DO want the mobile 0418 365 907 (in larger text)
I DO want:
My name: Dennis Harlow-Pike
I DO want: Australian Credit Licence 512964 (Tallow Creek Pty Ltd)
I DO want: Principal Finance Broker
I DO want new email: dennis@plantreasurepath.com.au
I DO want address: PO Box 836, Marrowvale Qld 4873
I DO want the existing logo (PTP on existing card)

Target Market(s)

Business Borrowers, Home Purchasers, and People wanting to finance cars and plant and equipment

Industry/Entity Type

Financial Service

Contact Information for Business Card

See project description

Font styles to use
Serif

Colors

Designer to choose colors to be used in the design.

Requirements
Must have
• See project description
Nice to have
• Black and Yellow colours
Should not have
• See project description

```html
<!DOCTYPE html>
<html lang="en">
<head>
<meta charset="utf-8">
<title>Plan Treasure Path – Business Card</title>
<link rel="stylesheet" href="https://fonts.googleapis.com/css2?family=Tinos:wght@400;700&family=Jost:wght@400&display=swap">
<style>
  :root {
    --backdrop: #1b1b1b;
    --card-dark: #161616;
    --card-light: #ffffff;
    --ink: #1f1f1f;
    --lime: #dfe35c;
    --phone-box: #232a28;
    --emboss: #2c2c2c;
    --silver-light: #d2d2d2;
  }
  * { box-sizing: border-box; margin: 0; padding: 0; }
  html, body { width: 1200px; height: 900px; overflow: hidden; }
  body {
    background: var(--backdrop);
    font-family: "Tinos", "Times New Roman", serif;
    color: var(--ink);
  }
  .card {
    position: absolute;
    left: 280px;
    width: 640px;
    height: 390px;
    overflow: hidden;
  }
  .card--back { top: 40px; background: linear-gradient(135deg, #121212 0%, #1c1c1c 60%, #232323 100%); }
  .card--front { top: 470px; background: var(--card-light); }

  .brand { position: absolute; display: flex; align-items: center; gap: 16px; }
  .brand__text { display: flex; flex-direction: column; align-items: flex-start; }
  .brand__name {
    font-family: "Tinos", serif;
    font-weight: 700;
    font-size: 34px;
    line-height: 1;
    letter-spacing: 0.5px;
  }
  .brand__group {
    font-family: "Jost", sans-serif;
    font-size: 13px;
    letter-spacing: 1.5px;
    margin-top: 6px;
  }
  .brand__dot { width: 52px; height: 52px; border-radius: 50%; flex: none; }

  .card--back .brand { left: 110px; top: 162px; }
  .card--back .brand__name { color: var(--emboss); }
  .card--back .brand__group { color: var(--emboss); }
  .card--back .brand__dot { background: var(--silver-light); }

  .card--front .brand { left: 90px; top: 46px; }
  .card--front .brand__name { color: var(--ink); }
  .card--front .brand__group { color: var(--lime); }
  .card--front .brand__dot { background: var(--lime); }

  .holder {
    position: absolute;
    top: 140px;
    left: 0;
    width: 100%;
    text-align: center;
    line-height: 1.05;
  }
  .holder__name { font-size: 32px; letter-spacing: 0.5px; text-transform: uppercase; }
  .holder__role, .holder__licence { font-size: 22px; }

  .band {
    position: absolute;
    left: 0;
    top: 262px;
    width: 100%;
    height: 30px;
    background: var(--lime);
  }
  .phone {
    position: absolute;
    top: 252px;
    left: 210px;
    width: 230px;
    height: 50px;
    background: var(--phone-box);
    color: #fff;
    font-size: 32px;
    line-height: 50px;
    text-align: center;
    border-left: 5px solid #fff;
    border-right: 5px solid #fff;
  }
  .contact {
    position: absolute;
    top: 312px;
    left: 0;
    width: 100%;
    text-align: center;
    font-size: 21px;
    line-height: 1.2;
  }
</style>
</head>
<body>
  <section class="card card--back" aria-label="Card back">
    <div class="brand">
      <div class="brand__text">
        <span class="brand__name">Plan Treasure Path</span>
        <span class="brand__group">A Member of the Tallow Creek Group</span>
      </div>
      <span class="brand__dot"></span>
    </div>
  </section>

  <section class="card card--front" aria-label="Card front">
    <div class="brand">
      <div class="brand__text">
        <span class="brand__name">Plan Treasure Path</span>
        <span class="brand__group">A Member of the Tallow Creek Group</span>
      </div>
      <span class="brand__dot"></span>
    </div>

    <div class="holder">
      <p class="holder__name">Dennis Harlow-Pike</p>
      <p class="holder__role">Principal Finance Broker</p>
      <p class="holder__licence">Australian Credit Licence 512964</p>
    </div>

    <div class="band"></div>
    <div class="phone">0418 365 907</div>

    <div class="contact">
      <p class="contact__email">dennis@plantreasurepath.com.au</p>
      <p class="contact__address">PO Box 836, Marrowvale Qld 4873</p>
    </div>
  </section>
</body>
</html>
```